Mini-Banner für Rubriken
Hallo,
wir benötigen für unsere Seite www.quilmar.de neue und vorallem passende Banner für die Highlights (rechte Seite) innerhalb der Rubriken, wie z.B. All Inklusive, Wellness, Urlaub an der Küste u.s.w. Vielen Dank für die Vorschläge !

```html
<!DOCTYPE html>
<html lang="de">
<head>
<meta charset="utf-8">
<title>Mini-Banner für Rubriken – quilmar stays</title>
<link rel="stylesheet" href="https://fonts.googleapis.com/css2?family=Righteous&display=swap">
<style>
  :root {
    --page: #ffffff;
    --outline: #ffffff;

    --allin-bg-left: #4a44ff;
    --allin-bg-right: #8d8ad8;
    --allin-top: #4b3ef5;
    --allin-bottom: #a24ff5;

    --well-bg-left: #ff4b10;
    --well-bg-right: #e6907a;
    --well-top: #dfb00e;
    --well-bottom: #ff4d12;

    --coast-bg-left: #8cf0c6;
    --coast-bg-right: #a9d8c6;
    --coast-top: #8ef0c4;
    --coast-bottom: #3a7af5;
  }
  * { margin: 0; padding: 0; box-sizing: border-box; }
  html, body {
    width: 1200px; height: 1200px; overflow: hidden;
    background: var(--page);
  }
  .banner-stack { position: relative; width: 1200px; height: 1200px; }
  .category-banner {
    position: absolute; left: 0; width: 1197px; height: 381px; overflow: hidden;
  }
  .category-banner--allin { top: 0; }
  .category-banner--wellness { top: 409px; }
  .category-banner--coast { top: 816px; }

  .banner-photo { position: absolute; inset: 0; }
  .category-banner--allin .banner-photo {
    background: linear-gradient(90deg, var(--allin-bg-left) 0%, var(--allin-bg-left) 30%, var(--allin-bg-right) 100%);
  }
  .category-banner--wellness .banner-photo {
    background: linear-gradient(90deg, var(--well-bg-left) 0%, var(--well-bg-left) 30%, var(--well-bg-right) 100%);
  }
  .category-banner--coast .banner-photo {
    background: linear-gradient(90deg, var(--coast-bg-left) 0%, var(--coast-bg-left) 30%, var(--coast-bg-right) 100%);
  }

  .banner-title { position: absolute; inset: 0; width: 1197px; height: 381px; }
  .banner-title text {
    font-family: 'Righteous', sans-serif;
    font-size: 190px;
  }
  .title-outline { fill: var(--outline); stroke: var(--outline); stroke-width: 14px; stroke-linejoin: round; }
  .category-banner--allin .title-bottom { fill: var(--allin-bottom); }
  .category-banner--allin .title-top { fill: var(--allin-top); }
  .category-banner--wellness .title-bottom { fill: var(--well-bottom); }
  .category-banner--wellness .title-top { fill: var(--well-top); }
  .category-banner--coast .title-bottom { fill: var(--coast-bottom); }
  .category-banner--coast .title-top { fill: var(--coast-top); }
</style>
</head>
<body>
<main class="banner-stack">

  <section class="category-banner category-banner--allin">
    <div class="banner-photo" role="img" aria-label="Strandfoto mit Muscheln und Steinen im Sand, blau getönt"></div>
    <svg class="banner-title" viewBox="0 0 1197 381" role="img" aria-label="All Inklusive">
      <defs>
        <clipPath id="wave-allin"><path d="M0 222 C300 200 600 232 1197 196 L1197 0 L0 0 Z"/></clipPath>
      </defs>
      <text class="title-outline" x="130" y="275" textLength="957" lengthAdjust="spacingAndGlyphs">All Inklusive</text>
      <text class="title-bottom" x="130" y="275" textLength="957" lengthAdjust="spacingAndGlyphs">All Inklusive</text>
      <text class="title-top" x="130" y="275" textLength="957" lengthAdjust="spacingAndGlyphs" clip-path="url(#wave-allin)">All Inklusive</text>
    </svg>
  </section>

  <section class="category-banner category-banner--wellness">
    <div class="banner-photo" role="img" aria-label="Strandfoto mit Muscheln und Steinen im Sand, orange getönt"></div>
    <svg class="banner-title" viewBox="0 0 1197 381" role="img" aria-label="Wellness">
      <defs>
        <clipPath id="wave-wellness"><path d="M0 205 C300 190 600 212 1197 192 L1197 0 L0 0 Z"/></clipPath>
      </defs>
      <text class="title-outline" x="233" y="262" textLength="747" lengthAdjust="spacingAndGlyphs">Wellness</text>
      <text class="title-bottom" x="233" y="262" textLength="747" lengthAdjust="spacingAndGlyphs">Wellness</text>
      <text class="title-top" x="233" y="262" textLength="747" lengthAdjust="spacingAndGlyphs" clip-path="url(#wave-wellness)">Wellness</text>
    </svg>
  </section>

  <section class="category-banner category-banner--coast">
    <div class="banner-photo" role="img" aria-label="Strandfoto mit Muscheln und Steinen im Sand, mintgrün getönt"></div>
    <svg class="banner-title" viewBox="0 0 1197 381" role="img" aria-label="Urlaub an der Küste">
      <defs>
        <clipPath id="wave-coast">
          <path d="M0 114 C300 98 600 122 1197 100 L1197 0 L0 0 Z"/>
          <path d="M0 276 C300 262 600 284 1197 262 L1197 190 L0 190 Z"/>
        </clipPath>
      </defs>
      <text class="title-outline" x="187" y="179" textLength="835" lengthAdjust="spacingAndGlyphs">Urlaub an</text>
      <text class="title-outline" x="207" y="340" textLength="811" lengthAdjust="spacingAndGlyphs">der Küste</text>
      <text class="title-bottom" x="187" y="179" textLength="835" lengthAdjust="spacingAndGlyphs">Urlaub an</text>
      <text class="title-bottom" x="207" y="340" textLength="811" lengthAdjust="spacingAndGlyphs">der Küste</text>
      <g clip-path="url(#wave-coast)">
        <text class="title-top" x="187" y="179" textLength="835" lengthAdjust="spacingAndGlyphs">Urlaub an</text>
        <text class="title-top" x="207" y="340" textLength="811" lengthAdjust="spacingAndGlyphs">der Küste</text>
      </g>
    </svg>
  </section>

</main>
</body>
</html>
```